Healthy snack food company needs a package design

We need a package design for a dry roasted flax seed snack. Consumers are not familiar with the concept of eating seasoned roasted flax as an on-the-go snack, so we want to break the image of flax being only used as an ingredient. It is very important to capture the idea of pouring the flax seeds into a hand and consuming directly. This product will compete with other nuts, chips, snack items in stores. Our seeds are crunchy and flavored with Chili Lime Seasoning to make them an irresistible snack, that also happens to be extremely good for you. This product will come in a 5oz stand up pouch bag with zip closure and peg hook hole at the top.

Target Market(s)

Individuals and families of all age groups seeking a healthy snacking option

Industry/Entity Type

Consumer

Font styles to use
Sans Serif

Requirements
Must have
• - Image/sketch of roasted flax seed in an appetizing/creative manner that conveys on the go snacking. Product to be eaten by hand, so a graphic illustration/sketch showing the flax seeds being poured in hand and eaten (pour - enjoy - repeat) for example
• - Product callouts: “Roasted Flax Seed”; “Read-To-Eat Snack” “Chili Lime” flavor
• - Company Name: Tovela (we are not providing the logo because we don’t want that to influence the package design)
Nice to have
• - Creative identity: Premium, Fun
• -Product claims include Organic, Non-GMO, High in fiber, protein, omega-3, iron. These don’t need to be called out, just sharing if desired to incorporate
Should not have
• No see through window

```html
<!DOCTYPE html>
<html lang="en">
<head>
<meta charset="utf-8">
<title>Tovela Roasted Flax Seed – Pouch Front</title>
<link rel="stylesheet" href="https://fonts.googleapis.com/css2?family=Open+Sans:wght@400;600;700;800&display=swap">
<style>
  :root {
    --backdrop: #e4e3e1;
    --gold-light: #d9c77f;
    --gold-mid: #c7b262;
    --gold-deep: #a8924a;
    --cocoa: #3b1f14;
    --cocoa-ink: #4a2a1c;
    --chili: #8a3a1e;
    --seed-brown: #6a3e2a;
    --seed-dark: #3a2117;
    --wood: #c9a574;
    --badge: #7a4a36;
    --white: #ffffff;
  }
  html, body {
    margin: 0;
    padding: 0;
    width: 1200px;
    height: 987px;
    overflow: hidden;
    background: var(--backdrop);
  }
  .canvas {
    position: relative;
    width: 1200px;
    height: 987px;
  }
  .pouch {
    position: absolute;
    left: 370px;
    top: 120px;
    width: 460px;
    height: 740px;
    background: linear-gradient(160deg, var(--gold-light) 0%, var(--gold-mid) 45%, var(--gold-deep) 100%);
    overflow: hidden;
    clip-path: polygon(0 0, 100% 0, 100% 14%, 98.5% 15%, 100% 16%, 100% 100%, 0 100%, 0 16%, 1.5% 15%, 0 14%);
    font-family: "Open Sans", sans-serif;
  }
  .hang-tab {
    position: absolute;
    left: 20%;
    top: 0;
    width: 60%;
    height: 58px;
    background: var(--cocoa);
  }
  .seal-line {
    position: absolute;
    left: 0;
    right: 0;
    top: 104px;
    height: 6px;
    background: rgba(0, 0, 0, 0.06);
  }
  .brand {
    position: absolute;
    top: 232px;
    left: 0;
    right: 0;
    margin: 0;
    text-align: center;
    font-size: 60px;
    font-weight: 800;
    color: var(--cocoa-ink);
    line-height: 1;
    letter-spacing: 0.5px;
  }
  .product-name {
    position: absolute;
    top: 304px;
    left: 0;
    right: 0;
    margin: 0;
    text-align: center;
    font-size: 34px;
    font-weight: 600;
    color: var(--cocoa-ink);
    line-height: 1;
  }
  .flavor {
    position: absolute;
    top: 352px;
    left: 0;
    right: 0;
    margin: 0;
    text-align: center;
    font-size: 22px;
    font-weight: 700;
    color: var(--chili);
    line-height: 1;
    text-transform: uppercase;
    letter-spacing: 2px;
  }
  .snack-callout {
    position: absolute;
    top: 384px;
    left: 0;
    right: 0;
    margin: 0;
    text-align: center;
    font-size: 15px;
    font-weight: 600;
    color: var(--cocoa-ink);
    line-height: 1;
    letter-spacing: 1px;
  }
  .product-photo {
    position: absolute;
    left: 0;
    right: 0;
    top: 440px;
    bottom: 0;
    background:
      radial-gradient(ellipse 45% 30% at 40% 62%, var(--wood) 0%, rgba(201,165,116,0) 75%),
      radial-gradient(ellipse 80% 60% at 50% 55%, var(--seed-brown) 0%, var(--seed-dark) 100%);
  }
  .photo-fade {
    position: absolute;
    left: 0;
    right: 0;
    top: 440px;
    height: 80px;
    background: linear-gradient(to bottom, var(--gold-deep), rgba(168,146,74,0));
  }
  .tagline {
    position: absolute;
    top: 450px;
    left: 0;
    right: 0;
    margin: 0;
    text-align: center;
    font-size: 14px;
    font-weight: 400;
    color: var(--cocoa-ink);
  }
  .claim-badge {
    position: absolute;
    left: 20px;
    bottom: 70px;
    width: 70px;
    height: 70px;
    background: var(--badge);
    color: var(--white);
    text-align: center;
    display: flex;
    flex-direction: column;
    justify-content: center;
    line-height: 1.15;
  }
  .claim-badge strong { font-size: 19px; font-weight: 700; }
  .claim-badge span { font-size: 14px; }
  .net-weight {
    position: absolute;
    right: 26px;
    bottom: 20px;
    text-align: right;
    color: var(--white);
    line-height: 1.1;
  }
  .net-weight .label { font-size: 12px; display: block; }
  .net-weight .amount { font-size: 16px; font-weight: 700; display: block; }
</style>
</head>
<body>
<main class="canvas">
  <section class="pouch">
    <div class="hang-tab"></div>
    <div class="seal-line"></div>
    <h1 class="brand">Tovela</h1>
    <p class="product-name">Roasted Flax Seed</p>
    <p class="flavor">Chili Lime</p>
    <p class="snack-callout">Ready-To-Eat Snack</p>
    <div class="product-photo" role="img" aria-label="Photo of roasted flax seeds heaped in a wooden bowl with a wooden spoon, ready to pour into a hand"></div>
    <div class="photo-fade"></div>
    <p class="tagline">Contains Nothing Artificial</p>
    <div class="claim-badge"><strong>GMO</strong><span>Free</span></div>
    <div class="net-weight"><span class="label">Net Weight</span><span class="amount">5oz</span></div>
  </section>
</main>
</body>
</html>
```